Author needs a new book, Kindle and Audiobook cover design

I updated and re-edited a book I wrote 25 years ago but now realize the title and design did not get the job done. I am seeking a book, Kindle and audiobook design that will make me stand out. The final design will pop while being sensitive to the nature of the subject. The title of the book is Quiet Lanterns. Subtitle: Ways to Notice and Step Away From Harmful Circles While Keeping Steady Belief by Dorian T. Wexcombe. I am wanting to get the attention of people who have been damaged by a church relationship that started well but ended badly.
Updates

The book title is: Quiet Lanterns. The Subtitle is: Ways To Notice and Step Away From Harmful Circles While Keeping Steady Belief. The dimension is 6x9 (150 pages) and I am the author: Dorian T. Wexcombe

Target Market(s)

People with a church experience; church leadership. Religious abuse victims.

Industry/Entity Type

Christian

Font styles to use
Serif

Colors

Designer to choose colors to be used in the design.

Requirements
Nice to have
• I am not married to the Serif font if another design works better.

```html
<!DOCTYPE html>
<html lang="en">
<head>
<meta charset="utf-8">
<title>Quiet Lanterns — Full Cover Wrap</title>
<link rel="stylesheet" href="https://fonts.googleapis.com/css2?family=Playfair+Display:ital,wght@0,700;0,900;1,700&family=Montserrat:wght@500;600;800&display=swap">
<style>
  :root {
    --backdrop: #f6c6c3;
    --gold: #e9a91c;
    --gold-deep: #c98710;
    --gold-light: #f6cf5a;
    --ink: #141414;
    --text: #2a2a2a;
    --paper: #ffffff;
    --sky-top: #f3dfa6;
    --sky-mid: #e9b552;
    --field: #6d4a1c;
  }
  * { box-sizing: border-box; margin: 0; padding: 0; }
  html, body { width: 800px; height: 1200px; overflow: hidden; background: var(--backdrop); }
  .canvas { position: relative; width: 800px; height: 1200px; }

  .wrap {
    position: absolute;
    left: 0; top: 322px;
    width: 800px; height: 555px;
    display: flex;
    box-shadow: 0 6px 18px rgba(0,0,0,0.18);
  }

  /* ---------- back cover ---------- */
  .back {
    position: relative;
    width: 370px; height: 555px;
    background: var(--paper);
    overflow: hidden;
  }
  .praise { position: absolute; left: 22px; right: 22px; top: 22px; }
  .praise-item { margin-bottom: 18px; }
  .praise-quote {
    font-family: "Montserrat", Arial, sans-serif;
    font-weight: 500;
    font-size: 8px;
    line-height: 1.5;
    color: var(--text);
  }
  .praise-source {
    margin-top: 5px;
    font-family: "Montserrat", Arial, sans-serif;
    font-weight: 800;
    font-size: 8px;
    color: var(--ink);
  }
  .praise-source .role { color: var(--gold-deep); }
  .back-band {
    position: absolute;
    left: 0; top: 330px;
    width: 370px; height: 180px;
    background: linear-gradient(90deg, var(--gold-deep) 0%, var(--gold-light) 55%, var(--gold-deep) 100%);
  }
  .author-photo {
    position: absolute;
    left: 22px; top: 22px;
    width: 112px; height: 136px;
    background: linear-gradient(180deg, #d9d2c6 0%, #9c8f7c 100%);
    border: 3px solid var(--paper);
  }
  .author-bio {
    position: absolute;
    left: 150px; right: 20px; top: 26px;
    font-family: "Montserrat", Arial, sans-serif;
    font-weight: 600;
    font-size: 8.5px;
    line-height: 1.55;
    color: var(--ink);
  }
  .back-strip, .front-strip {
    position: absolute;
    left: 0; bottom: 0;
    width: 100%; height: 45px;
    background: var(--ink);
  }

  /* ---------- spine ---------- */
  .spine {
    position: relative;
    width: 60px; height: 555px;
    background: var(--ink);
    overflow: hidden;
  }
  .spine-text {
    position: absolute;
    left: 0; top: 14px;
    width: 60px; height: 480px;
    writing-mode: vertical-rl;
    display: flex;
    align-items: center;
    justify-content: flex-start;
    gap: 16px;
  }
  .spine-subtitle {
    font-family: "Montserrat", Arial, sans-serif;
    font-weight: 800;
    font-size: 6px;
    line-height: 1.4;
    text-transform: uppercase;
    color: var(--paper);
    width: 180px;
    text-align: center;
  }
  .spine-subtitle .accent { color: var(--gold); }
  .spine-title {
    font-family: "Playfair Display", Georgia, serif;
    font-weight: 900;
    font-size: 17px;
    letter-spacing: 1px;
    color: var(--gold);
    white-space: nowrap;
  }
  .spine-author {
    font-family: "Playfair Display", Georgia, serif;
    font-weight: 900;
    font-size: 11px;
    letter-spacing: 1px;
    text-transform: uppercase;
    color: var(--paper);
    white-space: nowrap;
  }
  .spine-foot {
    position: absolute;
    left: 0; bottom: 0;
    width: 60px; height: 45px;
    background: linear-gradient(90deg, var(--gold-deep), var(--gold-light), var(--gold-deep));
  }

  /* ---------- front cover ---------- */
  .front {
    position: relative;
    width: 370px; height: 555px;
    background: var(--paper);
    overflow: hidden;
  }
  .front-scene {
    position: absolute;
    left: 0; top: 0;
    width: 370px; height: 290px;
    background:
      radial-gradient(ellipse at 68% 60%, rgba(255,244,200,0.95) 0%, rgba(246,205,110,0.6) 25%, rgba(233,181,82,0) 55%),
      linear-gradient(180deg, var(--sky-top) 0%, var(--sky-mid) 55%, var(--field) 100%);
  }
  .scene-fade {
    position: absolute;
    left: 0; top: 200px;
    width: 370px; height: 90px;
    background: linear-gradient(180deg, rgba(255,255,255,0) 0%, var(--paper) 100%);
  }
  .title {
    position: absolute;
    left: 0; right: 0; top: 214px;
    text-align: center;
  }
  .title-lead {
    display: block;
    font-family: "Playfair Display", Georgia, serif;
    font-style: italic;
    font-weight: 700;
    font-size: 50px;
    line-height: 1;
    color: var(--gold);
  }
  .title-main {
    display: block;
    font-family: "Playfair Display", Georgia, serif;
    font-weight: 900;
    font-size: 46px;
    letter-spacing: 2px;
    line-height: 1.05;
    color: var(--ink);
  }
  .subtitle {
    position: absolute;
    left: 26px; right: 26px; top: 340px;
    text-align: center;
    font-family: "Montserrat", Arial, sans-serif;
    font-weight: 800;
    font-size: 11.5px;
    line-height: 1.4;
    text-transform: uppercase;
    color: var(--ink);
  }
  .subtitle .accent { color: var(--gold); }
  .byline {
    position: absolute;
    left: 0; right: 0; top: 402px;
    text-align: center;
    font-family: "Playfair Display", Georgia, serif;
    font-weight: 700;
    font-style: italic;
    font-size: 15px;
    color: var(--gold-deep);
  }
  .byline::before, .byline::after {
    content: "";
    display: inline-block;
    width: 60px; height: 1.5px;
    background: var(--gold);
    vertical-align: middle;
    margin: 0 10px;
  }
  .author-band {
    position: absolute;
    left: 0; top: 440px;
    width: 370px; height: 70px;
    background: linear-gradient(90deg, var(--gold-deep) 0%, var(--gold-light) 50%, var(--gold-deep) 100%);
    display: flex;
    align-items: center;
    justify-content: center;
  }
  .author-name {
    font-family: "Playfair Display", Georgia, serif;
    font-weight: 900;
    font-size: 24px;
    letter-spacing: 1px;
    text-transform: uppercase;
    white-space: nowrap;
    color: var(--ink);
  }
</style>
</head>
<body>
  <div class="canvas">
    <div class="wrap">

      <section class="back">
        <div class="praise">
          <div class="praise-item">
            <p class="praise-quote">“A careful and gentle guide for anyone who has felt worn down inside a group that once felt like home. These pages name hard things plainly and still leave room for hope, healing and a steadier walk ahead.”</p>
            <p class="praise-source">Marlow Fenn, <span class="role">Senior Pastor, Brookhaven Fellowship</span></p>
          </div>
          <div class="praise-item">
            <p class="praise-quote">“Clear, honest and kind. The author writes from long experience and helps readers sort what was true from what was harmful, without tearing down faith itself.”</p>
            <p class="praise-source">Ivo Larkin, <span class="role">Ministry Leader</span></p>
          </div>
          <div class="praise-item">
            <p class="praise-quote">“A book I will hand to friends who are hurting. It is wise, practical and full of grace from the first page to the last.”</p>
            <p class="praise-source">Reed Alcott, <span class="role">Author</span></p>
          </div>
        </div>
        <div class="back-band">
          <div class="author-photo" role="img" aria-label="Portrait photograph of the author"></div>
          <p class="author-bio">Dorian T. Wexcombe has served for many years as a pastor, teacher and writer. He lives with his family and continues to help people find rest after hard seasons in church life.</p>
        </div>
        <div class="back-strip"></div>
      </section>

      <section class="spine">
        <div class="spine-text">
          <p class="spine-subtitle">Ways To <span class="accent">Notice</span> and <span class="accent">Step Away</span> From Harmful Circles While Keeping Steady Belief</p>
          <p class="spine-title">QUIET LANTERNS</p>
          <p class="spine-author">Dorian T. Wexcombe</p>
        </div>
        <div class="spine-foot"></div>
      </section>

      <section class="front">
        <div class="front-scene" role="img" aria-label="Photograph of a golden sunset over a field behind a barbed wire fence with birds flying free"></div>
        <div class="scene-fade"></div>
        <h1 class="title">
          <span class="title-lead">Quiet</span>
          <span class="title-main">LANTERNS</span>
        </h1>
        <p class="subtitle">Ways to <span class="accent">Notice</span> and <span class="accent">Step Away</span> From Harmful Circles While Keeping Steady Belief</p>
        <p class="byline">by</p>
        <div class="author-band">
          <p class="author-name">Dorian T. Wexcombe</p>
        </div>
        <div class="front-strip"></div>
      </section>

    </div>
  </div>
</body>
</html>
```